WE ARE REACHING OUT TO CONTRACTORS TO HAVE AN OPPORTUNITY TO PROVIDE PROPOSALS FOR THEIR PROJECTS.

WE ARE A WASHINGTON DC. METRO AREA PLUMBING, HEATING AND AIR CONDITIONING CONTRACTOR. WE WOULD LIKE TO PRESENT A POSTCARD THAT OFFERS A FRENDLY, CONVENIENT WAY TO PROVIDE PROPOSALS FOR THEIR UP COMMING PROJECTS. WE WOULD APPRECIATE THE OPPURTUNITY TO PROVIDE ESTIMATES FOR YOUR UP COMMING PROJECTS. IF REQUESTED, WE WILL PROVIDE SAME DAY WALK THRU'S AND PROPOSALS. GET A 2ND OPINION, WE ALL LOOK AT PROJECTS DIFFERENTLY. CUSTOM HOMES, SUB DIVISIONS, REMODELING, SEWER AND WATER INSTALLATIONS AND REPLACEMENTS, WELL AND SEPTIC INSTALLATIONS AND REPAIRS, MECHANICAL EQUIPTMENT CHANGE OUTS, PLUMBING SYSTEMS REPLACEMENTS AND REPAIRS. RESIDENTAL AND COMERICAL CONSTRUCTION.. " WE DO IT ALL" JUST GIVE US A CALL. " WE WILL BE THERE " I WOULD LIKE MY BUSINESS CARD ON THE FRONT WITH SOME MODIFICATIONS AND THE ABOVE DESCRIPTION ON THE BACK. " HIGHLIGHTING WE WOULD APPRICATE THE OPPORTUNITY TO WORK WITH YOU COMPANY " SAME DAY WALK THRU'S AND PROPOSALS. PLEASE ADDRESS THE TOP OF THE BACK IN BOLD PRINT. " ATTENTION ESTIMATING " EYE CATCHING COLORS PLEASE. THANK YOU, TODD WEMLEY

```html
<!DOCTYPE html>
<html lang="en">
<head>
<meta charset="utf-8">
<title>T.R.Wemley Mechanical Services – Estimating Postcard</title>
<link rel="stylesheet" href="https://fonts.googleapis.com/css2?family=Saira:wdth,wght@100..125,300..800&display=swap">
<style>
  :root {
    --red: #e31e26;
    --red-dark: #c8161d;
    --white: #ffffff;
    --ink: #231f20;
    --grey-text: #8a8a8a;
    --stage: #ececec;
    --panel-light: #f4f4f4;
    --panel-mid: #e2e2e2;
  }
  * { box-sizing: border-box; margin: 0; padding: 0; }
  html, body {
    width: 1200px; height: 1000px; overflow: hidden;
    background: var(--stage);
    font-family: "Saira", "Arial", sans-serif;
    font-stretch: 118%;
  }
  .canvas { position: relative; width: 1200px; height: 1000px; }

  .card { position: absolute; width: 462px; height: 333px; overflow: hidden; }
  .card--front { left: 105px; top: 302px; background: var(--red); }
  .card--back { left: 637px; top: 301px; background: linear-gradient(180deg, var(--panel-light) 0%, var(--panel-mid) 100%); }
  .card svg.deco { position: absolute; display: block; }

  /* Front */
  .front-top { position: absolute; left: 0; top: 0; width: 100%; height: 105px; background: var(--white); }
  .brand { position: absolute; left: 0; top: 36px; width: 100%; display: flex; justify-content: center; align-items: center; gap: 10px; }
  .brand__mark { width: 22px; height: 22px; background: var(--red); }
  .brand__name { color: var(--red); font-weight: 600; font-size: 21px; line-height: 1; letter-spacing: 0.2px; }
  .brand__name small { display: block; font-size: 10.5px; margin-top: 3px; letter-spacing: 0.4px; }
  .brand-shadow { left: 105px; top: 84px; }

  .name-tag { position: absolute; left: 3px; top: 143px; width: 187px; height: 35px; background: var(--white);
    color: var(--red); font-weight: 600; font-size: 19px; line-height: 35px; padding-left: 30px; }
  .name-shadow { left: 30px; top: 178px; }
  .divider { position: absolute; left: 226px; top: 150px; width: 1px; height: 70px; background: rgba(255,255,255,0.7); }

  .contact { position: absolute; left: 33px; top: 210px; color: var(--white); }
  .contact__phone { font-size: 20px; font-weight: 600; line-height: 1.1; }
  .contact__email { font-size: 12px; font-weight: 500; margin-top: 2px; }
  .contact__address { font-size: 12px; font-weight: 500; margin-top: 24px; line-height: 1.3; }

  .experience { position: absolute; left: 248px; top: 140px; color: var(--white); }
  .experience__years { font-size: 22px; font-weight: 300; line-height: 1.1; }
  .experience__scope { font-size: 10px; font-weight: 400; line-height: 1.25; }

  .services { position: absolute; left: 248px; top: 212px; list-style: none; color: var(--white); }
  .services li { font-size: 16px; font-weight: 600; line-height: 23px; }
  .front-stripes { right: 0; top: 212px; }

  /* Back */
  .back-header { position: absolute; left: 0; top: 0; width: 100%; height: 106px; background: var(--red); }
  .back-title { position: absolute; left: 0; top: 22px; width: 100%; text-align: center; font-weight: 800; font-size: 30px; line-height: 28px; }
  .back-title__top { color: var(--white); display: block; }
  .back-title__bottom { color: var(--ink); display: block; }
  .title-shadow { left: 105px; top: 82px; }
  .stripes-left { left: 0; top: 26px; }
  .stripes-right { right: 0; top: 26px; }

  .pitch { position: absolute; left: 25px; top: 120px; width: 228px; font-size: 10px; line-height: 12.5px; color: var(--ink); font-weight: 400; }
  .pitch p + p { margin-top: 8px; }
  .pitch .highlight { color: var(--red); font-weight: 600; }

  .slogan { position: absolute; left: 266px; top: 122px; font-size: 15px; line-height: 18px; }
  .slogan__accent { color: var(--red); font-weight: 700; display: block; }
  .slogan__plain { color: var(--ink); font-weight: 400; display: block; }

  .address-box { position: absolute; left: 263px; top: 192px; width: 175px; height: 109px; background: var(--white);
    border: 1px solid #cfcfcf; box-shadow: 1px 2px 3px rgba(0,0,0,0.25);
    display: flex; align-items: center; justify-content: center; color: var(--grey-text); font-size: 15px; font-weight: 400; }
</style>
</head>
<body>
<div class="canvas">

  <section class="card card--front" aria-label="Business card front">
    <div class="front-top">
      <div class="brand">
        <span class="brand__mark"></span>
        <span class="brand__name">T.R.WEMLEY<small>MECHANICAL SERVICES</small></span>
      </div>
    </div>
    <svg class="deco brand-shadow" width="252" height="10" viewBox="0 0 252 10" aria-hidden="true">
      <defs><linearGradient id="swoosh" x1="0" x2="1"><stop offset="0" stop-color="#999" stop-opacity="0"/><stop offset="0.5" stop-color="#555"/><stop offset="1" stop-color="#999" stop-opacity="0"/></linearGradient></defs>
      <path d="M0 2 Q126 10 252 2 Q126 5 0 2Z" fill="url(#swoosh)"/>
    </svg>

    <div class="name-tag">TODD WEMLEY</div>
    <svg class="deco name-shadow" width="150" height="8" viewBox="0 0 150 8" aria-hidden="true">
      <defs><linearGradient id="nameSwoosh" x1="0" x2="1"><stop offset="0" stop-color="#000" stop-opacity="0"/><stop offset="0.5" stop-color="#000" stop-opacity="0.55"/><stop offset="1" stop-color="#000" stop-opacity="0"/></linearGradient></defs>
      <path d="M0 0 Q75 8 150 0Z" fill="url(#nameSwoosh)"/>
    </svg>

    <div class="divider"></div>

    <div class="experience">
      <div class="experience__years">36 YEARS</div>
      <div class="experience__scope">RESIDENTIAL AND COMMERCIAL<br>CONSTRUCTION AND REMODELING</div>
    </div>

    <div class="contact">
      <div class="contact__phone">301-555-0148</div>
      <div class="contact__email">TODDWEMLEY@MAILBOX.COM</div>
      <div class="contact__address">1180 ORCHARD HILL ROAD<br>WESTFIELD, MD 21770</div>
    </div>

    <ul class="services">
      <li>HEATING</li>
      <li>PLUMBING</li>
      <li>GAS FITTING</li>
      <li>AIR CONDITIONING</li>
    </ul>

    <svg class="deco front-stripes" width="86" height="82" viewBox="0 0 86 82" aria-hidden="true" fill="#fff">
      <polygon points="30,0 86,0 86,12 18,12"/>
      <polygon points="14,17 86,17 86,30 2,30"/>
      <polygon points="2,35 86,35 86,48 14,48"/>
      <polygon points="18,53 86,53 86,66 30,66"/>
      <polygon points="34,70 86,70 86,82 46,82" opacity="0"/>
    </svg>
  </section>

  <section class="card card--back" aria-label="Postcard back">
    <div class="back-header"></div>
    <svg class="deco stripes-left" width="56" height="36" viewBox="0 0 56 36" aria-hidden="true" fill="#fff">
      <polygon points="0,0 44,0 50,8 0,8"/>
      <polygon points="0,14 52,14 56,18 52,22 0,22"/>
      <polygon points="0,28 50,28 44,36 0,36"/>
    </svg>
    <svg class="deco stripes-right" width="56" height="36" viewBox="0 0 56 36" aria-hidden="true" fill="#fff">
      <polygon points="56,0 12,0 6,8 56,8"/>
      <polygon points="56,14 4,14 0,18 4,22 56,22"/>
      <polygon points="56,28 6,28 12,36 56,36"/>
    </svg>
    <h1 class="back-title"><span class="back-title__top">ATTENTION</span><span class="back-title__bottom">ESTIMATING</span></h1>
    <svg class="deco title-shadow" width="252" height="10" viewBox="0 0 252 10" aria-hidden="true">
      <defs><linearGradient id="titleSwoosh" x1="0" x2="1"><stop offset="0" stop-color="#000" stop-opacity="0"/><stop offset="0.5" stop-color="#000" stop-opacity="0.6"/><stop offset="1" stop-color="#000" stop-opacity="0"/></linearGradient></defs>
      <path d="M0 0 Q126 10 252 0Z" fill="url(#titleSwoosh)"/>
    </svg>

    <div class="pitch">
      <p><span class="highlight">We would appreciate the opportunity to provide estimates for your upcoming projects.</span> If requested, <span class="highlight">we will provide same day walk thru's and proposals</span>.</p>
      <p>Get a 2nd opinion,<br>we all look at projects differently.</p>
      <p>Custom homes, sub divisions, remodeling, sewer and water installations and replacements, well and septic installations and repairs, mechanical equipment change outs, plumbing systems replacements and repairs. Residential and commercial construction.</p>
    </div>

    <div class="slogan">
      <span class="slogan__accent">“WE DO IT ALL”</span>
      <span class="slogan__plain">JUST GIVE US A CALL.</span>
      <span class="slogan__accent">“WE WILL BE THERE”</span>
    </div>

    <div class="address-box">Address Here</div>
  </section>

</div>
</body>
</html>
```